TRV Construction and Remodeling

Prefer a matte black card with some colors that pop, but subtle. Contact info. Show General Contractor professional way. Can you please remove renovations repairs maintenance off of my logo.

Target Market(s)

Property and business investors. Homeowners

Industry/Entity Type

Construction

Contact Information for Business Card

Name: Dorian Vekkart, Title: CEO, Phone: 555-014-7392, Email: Dorian@TRVbuildNkx.example, website: www TRVbuildNkx.example

• Designer choose

Colors

Designer to choose colors to be used in the design.

Requirements
Must have
• Uniqueness. Double sided since it wont let me choose that. Professional look, be eye catching and catchy. QR code to my website
Nice to have
• Matte black background, subtle bright colors that pop, but I am open to anything. I also like black and gold with some red. Possible Harborton Ravens logo colored stars somewhere around the logo or on the back. Just to rep my city
Should not have
• pink. Something you would see somewhere else. gif pictures or generated pictures.

```html
<!DOCTYPE html>
<html lang="en">
<head>
<meta charset="utf-8">
<title>TRV Construction and Remodeling – Business Card</title>
<link href="https://fonts.googleapis.com/css2?family=Arimo:wght@400;700&display=swap" rel="stylesheet">
<style>
  :root {
    --backdrop: #e4e4e6;
    --card-white: #ffffff;
    --card-black: #2a2a2c;
    --ink: #2b2b2b;
    --ink-soft: #4a4a4a;
    --accent-red: #e30b1c;
    --emboss: #1c1c1e;
    --rule: #8a8a8a;
    --qr-fill: #3a3a3d;
  }
  * { box-sizing: border-box; margin: 0; padding: 0; }
  html, body {
    width: 1200px; height: 802px; overflow: hidden;
    background: var(--backdrop);
    font-family: "Arimo", Arial, sans-serif;
  }
  .stage {
    width: 1200px; height: 802px;
    display: flex; align-items: center; justify-content: center; gap: 40px;
  }
  .card {
    width: 525px; height: 300px; position: relative; overflow: hidden;
    box-shadow: 0 6px 18px rgba(0,0,0,0.18);
  }
  /* Front */
  .card-front { background: var(--card-white); }
  .brand {
    position: absolute; left: 44px; top: 62px;
    display: flex; align-items: center; gap: 10px;
  }
  .brand-square { width: 14px; height: 14px; background: var(--accent-red); flex: none; }
  .brand-name {
    font-weight: 700; font-size: 21px; line-height: 1.05; color: var(--ink);
    letter-spacing: 0.3px; width: 190px;
  }
  .divider {
    position: absolute; left: 262px; top: 58px; width: 1px; height: 76px;
    background: var(--rule);
  }
  .contact-list {
    position: absolute; left: 278px; top: 60px; list-style: none;
    font-size: 14px; color: var(--ink-soft);
  }
  .contact-list li { display: flex; align-items: center; gap: 8px; height: 24px; white-space: nowrap; }
  .contact-list .highlight { color: var(--accent-red); }
  .contact-icon { width: 13px; height: 13px; flex: none; }
  .person { position: absolute; left: 44px; top: 170px; width: 200px; }
  .person-name {
    color: var(--accent-red); font-size: 21px; letter-spacing: 0.5px; text-transform: uppercase;
    white-space: nowrap;
  }
  .person-title { color: var(--ink-soft); font-size: 15px; margin-top: 4px; text-align: right; }
  .address-band {
    position: absolute; left: 0; right: 0; top: 230px; height: 40px;
    background: var(--accent-red); color: var(--card-white);
    font-size: 14.5px; display: flex; align-items: center; padding-left: 168px;
  }
  /* Back */
  .card-back {
    background: var(--card-black);
    display: flex; align-items: center; justify-content: center;
  }
  .back-brand {
    font-weight: 700; font-size: 34px; line-height: 1.05; color: var(--emboss);
    text-align: center; letter-spacing: 1px;
  }
  .qr-slot {
    position: absolute; right: 22px; bottom: 22px; width: 64px; height: 64px;
    background: var(--qr-fill);
  }
</style>
</head>
<body>
<main class="stage">
  <section class="card card-front" aria-label="Card front">
    <div class="brand">
      <span class="brand-square"></span>
      <span class="brand-name">TRV Construction &amp; Remodeling</span>
    </div>
    <div class="divider"></div>
    <ul class="contact-list">
      <li>
        <svg class="contact-icon" viewBox="0 0 14 14"><circle cx="7" cy="7" r="7" fill="var(--accent-red)"/><path d="M4.3 3.8c.6-.5 1.2-.3 1.5.3l.5 1c.2.4 0 .8-.3 1l-.4.3c.4.9 1 1.5 1.9 1.9l.3-.4c.2-.3.6-.5 1-.3l1 .5c.6.3.8.9.3 1.5-.8.9-2.2.8-3.6-.3-1.3-1-2.2-2.2-2.5-3.2-.2-.9 0-1.7.3-2.3z" fill="#fff"/></svg>
        555.014.7392
      </li>
      <li>
        <svg class="contact-icon" viewBox="0 0 14 14"><rect x="1" y="3" width="12" height="8" fill="var(--accent-red)"/><path d="M1 3l6 4.5L13 3" stroke="#fff" stroke-width="1.2" fill="none"/></svg>
        Dorian@TRVbuildNkx.example
      </li>
      <li>
        <svg class="contact-icon" viewBox="0 0 14 14"><circle cx="7" cy="7" r="7" fill="var(--accent-red)"/><circle cx="7" cy="7" r="4" fill="none" stroke="#fff" stroke-width="1"/><path d="M3 7h8M7 3v8" stroke="#fff" stroke-width="1"/></svg>
        <span>www.<span class="highlight">TRVbuildNkx</span>.example</span>
      </li>
    </ul>
    <div class="person">
      <p class="person-name">Dorian Vekkart</p>
      <p class="person-title">CEO</p>
    </div>
    <div class="address-band">Your Address, City, State, Zip 0000</div>
  </section>

  <section class="card card-back" aria-label="Card back">
    <p class="back-brand">TRV Construction<br>&amp; Remodeling</p>
    <div class="qr-slot" role="img" aria-label="QR code linking to www.TRVbuildNkx.example"></div>
  </section>
</main>
</body>
</html>
```